Microlight Aircraft Website Project

Need a website designed, or at least a template made, that my web programmer can work with here. We are a new manufacturer of microlight aircraft & powered hang gliders. Our company name is Brisk Fern. We manufacture portable utility aircraft in the Light Sport category (formerly known as Ultralights or Microlights). Our particular design is a 2-seat powered hang glider and caters to those who want to go explore the backcountry. We are not necessarily aviation nuts, but more into the development of a flying utility vehicle for extreme exploration and expeditions. We have been importing these aircraft from 3 countries for 15 years and have supplied over 200 expedition-quality aircraft world-wide. We are now manufacturing here in the US.

Industry/Entity Type

Manufacturer

Coding

Coded - Design and coding required

```html
<!DOCTYPE html>
<html lang="en">
<head>
<meta charset="utf-8">
<title>Brisk Fern — Microlight Aircraft &amp; Powered Hang Gliders</title>
<link href="https://fonts.googleapis.com/css2?family=Raleway:wght@400;500;600;700;800&display=swap" rel="stylesheet">
<style>
:root{
  --blue:#0a8fd6;
  --blue-deep:#0b5fa8;
  --navy:#0b3d7e;
  --navy-dark:#08306a;
  --cyan:#26a9e8;
  --ink:#222a33;
  --text:#666c73;
  --muted:#9aa0a6;
  --rule:#dcdfe2;
  --white:#ffffff;
  --sky-top:#cfe4f3;
  --sky-mid:#e8f2fa;
}
*{box-sizing:border-box;margin:0;padding:0}
html,body{width:1200px;height:2244px;overflow:hidden}
body{font-family:"Raleway",Arial,sans-serif;color:var(--ink);background:var(--white);position:relative}
.abs{position:absolute}

/* header */
.site-header{position:absolute;left:0;top:0;width:1200px;height:102px;
  background:linear-gradient(180deg,#dcebf6 0%,#f3f8fc 60%,#ffffff 100%);
  border-bottom:1px solid #c7d2db;box-shadow:0 2px 4px rgba(0,0,0,.12);z-index:3}
.brand{position:absolute;left:163px;top:30px;display:flex;align-items:center;gap:10px}
.brand-dot{width:34px;height:34px;border-radius:50%;background:var(--blue-deep)}
.brand-name{font-weight:800;font-size:22px;color:var(--blue-deep);letter-spacing:.5px}
.top-bar{position:absolute;left:703px;top:0;height:30px;display:flex}
.top-phone{background:var(--cyan);color:#fff;font-weight:700;font-size:16px;display:flex;align-items:center;gap:9px;padding:0 20px 0 16px;
  clip-path:polygon(4% 0,100% 0,100% 100%,0 100%)}
.top-cta{background:var(--navy);color:#fff;font-weight:700;font-size:14px;display:flex;align-items:center;padding:0 22px 0 16px;
  clip-path:polygon(0 0,100% 0,93% 100%,0 100%)}
.main-nav{position:absolute;right:163px;top:66px;display:flex;align-items:center;font-size:13.5px;font-weight:700;color:#111}
.main-nav span{padding:0 14px;border-left:1px solid #c9d1d8;line-height:16px}
.main-nav .nav-home{border-left:none;padding-left:0;padding-right:14px;display:flex}

/* hero */
.hero{position:absolute;left:0;top:102px;width:1200px;height:482px;
  background:linear-gradient(180deg,#9fb6c9 0%,#c7b8a4 14%,#b35a2d 34%,#c2521d 55%,#8f2f12 80%,#6b2410 100%)}
.hero-arrow{position:absolute;top:228px}
.hero-title{position:absolute;left:640px;top:254px;width:396px;text-align:center;color:#fff;font-weight:800;font-size:31px;line-height:42px;text-transform:uppercase;text-shadow:0 2px 4px rgba(0,0,0,.55);white-space:nowrap}
.hero-dots{position:absolute;left:569px;top:440px;display:flex;gap:10px}
.hero-dots i{width:13px;height:13px;border-radius:50%;background:#fff;display:block}
.hero-dots i.on{background:var(--blue)}

/* welcome */
.welcome{position:absolute;left:0;top:584px;width:1200px;height:356px;
  background:linear-gradient(180deg,var(--sky-top) 0%,var(--sky-mid) 45%,#f7fbfe 100%);text-align:center}
.section-title{font-weight:400;font-size:36px;letter-spacing:.5px;text-transform:uppercase}
.section-title b{font-weight:800}
.welcome .section-title{position:absolute;left:0;width:1200px;top:64px;color:#2a2f35}
.title-rule{position:absolute;left:281px;top:130px;width:636px;height:2px;background:linear-gradient(90deg,transparent,#b9c3cc 30%,#b9c3cc 70%,transparent)}
.title-mark{position:absolute;left:586px;top:117px;width:28px;height:28px;border-radius:50%;background:var(--blue-deep);border:3px solid var(--sky-mid)}
.welcome-copy{position:absolute;left:196px;top:160px;width:808px;font-size:11px;line-height:22.4px;color:#333}
.btn{display:inline-flex;align-items:center;justify-content:center;background:linear-gradient(180deg,#1b8fd8,#0b63ad);color:#fff;font-weight:700;font-size:11px;text-transform:uppercase;border-radius:2px;box-shadow:0 2px 0 #08457d}
.welcome .btn{position:absolute;left:548px;top:266px;width:104px;height:33px;letter-spacing:.5px}

/* manufacture */
.manufacture{position:absolute;left:0;top:940px;width:1200px;height:448px;
  background:linear-gradient(180deg,#1f2a44 0%,#2b3956 30%,#3c4a4a 60%,#2d2d22 100%)}
.manufacture .section-title{position:absolute;left:0;width:1200px;top:44px;color:#fff;text-align:center}
.tab{position:absolute;top:109px;width:427px;height:55px;background:rgba(18,26,40,.82);border:1px solid #6f7b8c;border-radius:3px;
  display:flex;align-items:center;justify-content:center;gap:16px;color:#fff;font-size:21px;text-transform:uppercase}
.tab.is-active::after{content:"";position:absolute;left:66px;right:66px;bottom:6px;height:3px;background:#fff}
.tab-pointer{position:absolute;left:362px;top:164px;width:0;height:0;border-left:13px solid transparent;border-right:13px solid transparent;border-top:13px solid #141c2a}
.product{position:absolute;top:192px;width:209px;height:196px;background:#fff;padding:6px;box-shadow:0 3px 6px rgba(0,0,0,.4)}
.product-photo{width:197px;height:135px;background:linear-gradient(180deg,#7fb2dc,#a9cde8)}
.product-photo.green{background:linear-gradient(180deg,#5b7a3a,#3f5a2b)}
.product-photo.water{background:linear-gradient(180deg,#5d7388,#2c4253)}
.product-label{position:absolute;left:0;bottom:0;width:209px;height:49px;background:linear-gradient(180deg,#2aa3e6,#0b6cba);color:#fff;font-size:21px;display:flex;align-items:center;justify-content:center;text-transform:uppercase}
.slider-arrow{position:absolute;top:262px}

/* news & events */
.block-head{position:absolute;top:1440px;height:40px;border-bottom:1px solid var(--rule);display:flex;justify-content:space-between;align-items:flex-start}
.block-head h2{font-size:22px;font-weight:400;text-transform:uppercase;color:#222}
.block-head h2 b{font-weight:800}
.read-all{font-size:9.5px;font-weight:700;color:var(--blue);margin-top:10px;text-transform:uppercase}
.col-divider{position:absolute;left:598px;top:1436px;width:1px;height:310px;background:var(--rule)}
.item{position:absolute;display:flex;gap:16px;border-bottom:1px solid var(--rule)}
.thumb{flex:none;background:linear-gradient(180deg,#7ea0c3 0%,#a8b2b8 50%,#6c7a4c 100%)}
.thumb.event{background:linear-gradient(180deg,#8a6a4c,#3f3322)}
.item h3{font-size:12px;font-weight:700;color:#222;margin-bottom:7px}
.item h3 .date{font-weight:500;font-style:italic;font-size:10px;color:var(--blue);margin-left:10px;padding-left:10px;border-left:1px solid var(--rule)}
.item p{font-size:10.5px;line-height:17.5px;color:var(--muted)}
.item .more{font-size:9px;font-weight:700;color:var(--blue);text-transform:uppercase;margin-top:3px}

/* subscribe */
.subscribe{position:absolute;left:0;top:1791px;width:1200px;height:187px;background:linear-gradient(180deg,#b9d5ec 0%,#dcebf6 50%,#c9def0 100%)}
.sub-card{position:absolute;left:239px;top:52px;width:750px;height:93px;background:#fff;box-shadow:0 3px 6px rgba(0,0,0,.18);
  border-top:5px solid transparent;border-image:repeating-linear-gradient(135deg,var(--blue-deep) 0 10px,#fff 10px 16px,var(--cyan) 16px 26px,#fff 26px 32px) 5}
.sub-title{position:absolute;left:75px;top:20px;font-size:18px;font-weight:700;color:#333;line-height:22px}
.sub-title span{display:block;font-weight:400}
.social{position:absolute;top:31px;width:24px;height:24px;border-radius:50%}
.sub-input{position:absolute;left:374px;top:30px;width:232px;height:31px;border:1px solid #cfd4d8;font-size:10px;color:#999;display:flex;align-items:center;padding-left:10px}
.sub-card .btn{position:absolute;left:623px;top:30px;width:109px;height:31px;font-size:10px;border-radius:0}

/* footer */
.site-footer{position:absolute;left:0;top:1978px;width:1200px;height:266px;background:var(--navy);color:#fff}
.foot-col{position:absolute;top:54px}
.foot-col h4{font-size:14px;font-weight:700;text-transform:uppercase;padding-bottom:9px;border-bottom:1px solid #3f6aa3;margin-bottom:8px}
.foot-links li{list-style:none;font-size:10px;line-height:20px;text-transform:uppercase;color:#d6e2f2}
.foot-links li::before{content:"›";margin-right:8px;color:#8fb0d8}
.foot-divider{position:absolute;top:52px;width:1px;height:140px;background:#2d5a95}
.field{width:190px;border:1px solid #4a7ab8;background:var(--navy-dark);font-size:10px;color:#d6e2f2;padding:3px 6px;margin-bottom:6px;border-radius:2px}
.foot-submit{display:inline-block;background:var(--cyan);font-size:10px;font-weight:700;padding:3px 10px;border-radius:2px;margin-top:2px}
.contact-row{display:flex;gap:10px;font-size:10.5px;line-height:15px;color:#e3ecf7;margin-bottom:14px}
.foot-brand{position:absolute;left:882px;top:62px;width:170px;text-align:center}
.foot-brand .brand-dot{margin:0 auto 8px;background:#fff}
.foot-brand .name{font-weight:800;font-size:20px;color:#fff}
.foot-brand .copy{font-size:9.5px;font-weight:700;line-height:15px;margin-top:12px;white-space:nowrap}
</style>
</head>
<body>

<header class="site-header">
  <div class="brand"><span class="brand-dot"></span><span class="brand-name">BRISK FERN</span></div>
  <div class="top-bar">
    <div class="top-phone">
      <svg width="18" height="18" viewBox="0 0 18 18" aria-hidden="true"><circle cx="9" cy="9" r="8" fill="none" stroke="#fff" stroke-width="1.5"/><path d="M6 5l2 2-1 1c.5 1.2 1.4 2.1 2.6 2.6l1-1 2 2-1.2 1.2C8.5 12.5 5.6 9.6 4.9 6.2z" fill="#fff"/></svg>
      555 014 2290
    </div>
    <div class="top-cta">Get A Free Consultation</div>
  </div>
  <nav class="main-nav">
    <span class="nav-home"><svg width="22" height="19" viewBox="0 0 22 19" aria-label="Home"><path d="M11 1L1 10h3v8h5v-5h4v5h5v-8h3z" fill="#0b6cba"/></svg></span>
    <span>ABOUT US</span><span>READY TO FLY</span><span>GALLERY</span><span>DOWNLOADS</span><span>CONTACT US</span>
  </nav>
</header>

<section class="hero" role="img" aria-label="Two-seat powered hang glider flying over red sandstone canyon hoodoos at sunset">
  <svg class="hero-arrow" style="left:90px" width="24" height="48" viewBox="0 0 24 48" aria-hidden="true"><path d="M22 2L3 24l19 22" fill="none" stroke="#fff" stroke-width="2.5"/></svg>
  <svg class="hero-arrow" style="left:1090px" width="24" height="48" viewBox="0 0 24 48" aria-hidden="true"><path d="M2 2l19 22L2 46" fill="none" stroke="#fff" stroke-width="2.5"/></svg>
  <h1 class="hero-title">Giving the pleasure<br>of an amazing<br>flying experience!</h1>
  <div class="hero-dots"><i class="on"></i><i></i><i></i></div>
</section>

<section class="welcome">
  <h2 class="section-title">Welcome to <b>Brisk Fern</b></h2>
  <div class="title-rule"></div>
  <div class="title-mark"></div>
  <p class="welcome-copy">Lorem ipsum dolor sit amet, consectetuer adipiscing elit, sed diam nonummy nibh euismod tincidunt ut laoreet dolore magna aliquam erat volutpat. Ut wisi enim ad minim veniam, quis nostrud exerci tation ullamcorper suscipit lobortis nisl ut aliquip ex ea commodo consequat. Duis autem vel eum iriure dolor in hendrerit in vulputate velit esse molestie consequat, vel illum dolore eu feugiat nulla facilisis at vero eros et accumsan et iusto odio dignissim qui blandit praesent luptatum zzril delenit augue duis dolore te feugait nulla facilisi.</p>
  <span class="btn">Read&nbsp; More</span>
</section>

<section class="manufacture" role="img" aria-label="Underside of a hang glider wing above mountain landscape">
  <h2 class="section-title">We <b>Manufacture</b></h2>
  <div class="tab is-active" style="left:162px">
    <svg width="30" height="24" viewBox="0 0 30 24" aria-hidden="true"><path d="M2 12h26M18 12l-8-10h-3l4 10-4 10h3zM4 12l-2-5h2l3 5-3 5H2z" fill="var(--cyan)" stroke="var(--cyan)" stroke-width="2" stroke-linejoin="round"/></svg>
    Micro Light Aircraft
  </div>
  <div class="tab-pointer"></div>
  <div class="tab" style="left:610px">
    <svg width="32" height="20" viewBox="0 0 32 20" aria-hidden="true"><path d="M1 4L31 2 16 8zM16 8v8M11 18h10" fill="var(--cyan)" stroke="var(--cyan)" stroke-width="2"/></svg>
    Powered Hang Gliders
  </div>
  <svg class="slider-arrow" style="left:84px" width="22" height="50" viewBox="0 0 22 50" aria-hidden="true"><path d="M20 2L3 25l17 23" fill="none" stroke="#fff" stroke-width="2"/></svg>
  <svg class="slider-arrow" style="left:1094px" width="22" height="50" viewBox="0 0 22 50" aria-hidden="true"><path d="M2 2l17 23L2 48" fill="none" stroke="#fff" stroke-width="2"/></svg>
  <div class="product" style="left:162px"><div class="product-photo green" role="img" aria-label="White microlight aircraft flying over green fields"></div><div class="product-label">KR 420</div></div>
  <div class="product" style="left:383px"><div class="product-photo" role="img" aria-label="Microlight aircraft in a clear blue sky"></div><div class="product-label">Ridge 2R</div></div>
  <div class="product" style="left:606px"><div class="product-photo water" role="img" aria-label="Amphibious microlight landing on water with spray"></div><div class="product-label">Water Sports</div></div>
  <div class="product" style="left:827px"><div class="product-photo" role="img" aria-label="Powered hang glider trike flying in blue sky"></div><div class="product-label">KR 420</div></div>
</section>

<section class="news-events">
  <div class="block-head" style="left:163px;width:411px"><h2>Latest <b>News</b></h2><span class="read-all">Read all »</span></div>
  <div class="item" style="left:162px;top:1493px;width:412px;height:114px">
    <div class="thumb" style="width:90px;height:96px" role="img" aria-label="Hang glider pilot in flight over a valley"></div>
    <div><h3>Lorem Ipsum Dolor Consecte</h3><p>Sed ut perspiciatis unde omnis iste natus error sit voluptatem accusantium dolo remque laudantium, totam rem aperiam, eaque ipsa quae ab illo inventore veritatis</p><div class="more">Read more</div></div>
  </div>
  <div class="item" style="left:162px;top:1621px;width:412px;height:114px">
    <div class="thumb" style="width:90px;height:96px" role="img" aria-label="Hang glider pilot in flight over a valley"></div>
    <div><h3>Lorem Ipsum Dolor Consecte</h3><p>Sed ut perspiciatis unde omnis iste natus error sit voluptatem accusantium dolo remque laudantium, totam rem aperiam, eaque ipsa quae ab illo inventore veritatis</p><div class="more">Read more</div></div>
  </div>

  <div class="col-divider"></div>

  <div class="block-head" style="left:634px;width:406px"><h2>Upcoming <b>Events</b></h2><span class="read-all">Read all »</span></div>
  <div class="item" style="left:630px;top:1499px;width:410px;height:68px">
    <div class="thumb event" style="width:84px;height:51px" role="img" aria-label="Microlight aircraft parked on an airfield"></div>
    <div><h3>Lorem Ipsum Dolor Consecte<span class="date">on 29 April, 2016</span></h3><p>Sed ut perspiciatis unde omnis iste natus error sit voluptatem</p><div class="more">Read more</div></div>
  </div>
  <div class="item" style="left:630px;top:1580px;width:410px;height:70px">
    <div class="thumb event" style="width:84px;height:51px" role="img" aria-label="Microlight aircraft parked on an airfield"></div>
    <div><h3>Lorem Ipsum Dolor Consecte<span class="date">on 29 April, 2016</span></h3><p>Sed ut perspiciatis unde omnis iste natus error sit voluptatem</p><div class="more">Read more</div></div>
  </div>
  <div class="item" style="left:630px;top:1665px;width:410px;height:70px">
    <div class="thumb event" style="width:84px;height:51px" role="img" aria-label="Microlight aircraft parked on an airfield"></div>
    <div><h3>Lorem Ipsum Dolor Consecte<span class="date">on 29 April, 2016</span></h3><p>Sed ut perspiciatis unde omnis iste natus error sit voluptatem</p><div class="more">Read more</div></div>
  </div>
</section>

<section class="subscribe">
  <div class="sub-card">
    <svg class="abs" style="left:0;top:18px" width="62" height="52" viewBox="0 0 62 52" aria-hidden="true"><g fill="none" stroke="#d9dde1" stroke-width="2"><path d="M2 10l56-6 2 40-56 6z"/><path d="M2 10l30 20 26-26M4 50l20-24M60 44L38 24"/></g></svg>
    <div class="sub-title">SUBSCRIBE<span>for Latest News</span></div>
    <span class="social" style="left:254px;background:#3b5a99"></span>
    <span class="social" style="left:287px;background:#2aa3e6"></span>
    <span class="social" style="left:321px;background:#dd4b39"></span>
    <div class="sub-input">Enter email address</div>
    <span class="btn">Subscibe</span>
  </div>
</section>

<footer class="site-footer">
  <div class="foot-col" style="left:162px;width:107px">
    <h4>Quick Links</h4>
    <ul class="foot-links"><li>Home</li><li>About us</li><li>Ready to fly</li><li>Gallery</li><li>Downloads</li><li>Contact us</li></ul>
  </div>
  <div class="foot-divider" style="left:307px"></div>
  <div class="foot-col" style="left:347px;width:192px">
    <h4>Quick Inquiry</h4>
    <div class="field">Name</div>
    <div class="field">Email</div>
    <div class="field" style="height:36px">Message</div>
    <span class="foot-submit">Submit</span>
  </div>
  <div class="foot-divider" style="left:577px"></div>
  <div class="foot-col" style="left:618px;width:200px">
    <h4>Contact Details</h4>
    <div class="contact-row"><svg width="10" height="14" viewBox="0 0 10 14" aria-hidden="true"><path d="M5 0a5 5 0 015 5c0 3.5-5 9-5 9S0 8.5 0 5a5 5 0 015-5z" fill="var(--cyan)"/><circle cx="5" cy="5" r="1.8" fill="var(--navy)"/></svg><span>Brisk Fern, 123 euismod cidun ut laoreetmok laoreet dol magnak aliquam PG Feugait.</span></div>
    <div class="contact-row" style="font-weight:700"><svg width="12" height="12" viewBox="0 0 12 12" aria-hidden="true"><path d="M2 0l3 3-1.5 1.5c.8 1.7 2.2 3.1 4 4L9 7l3 3-1.8 1.8C5.5 11.5.5 6.5.2 1.8z" fill="var(--cyan)"/></svg><span>555 - 014 - 2290</span></div>
    <div class="contact-row"><svg width="12" height="9" viewBox="0 0 12 9" aria-hidden="true"><rect width="12" height="9" fill="var(--cyan)"/><path d="M0 0l6 5 6-5" fill="none" stroke="var(--navy)"/></svg><span>info@briskfern.com</span></div>
  </div>
  <div class="foot-divider" style="left:856px"></div>
  <div class="foot-brand">
    <div class="brand-dot"></div>
    <div class="name">BRISK FERN</div>
    <div class="copy">Copyright © 2016 BRISK FERN.<br>All Right Reserved.</div>
  </div>
</footer>

</body>
</html>
```